Korvane Sky Works, LLC - Business Card

I currently have a drone business that specializes in aerial photography, thermal image inspections, deer recovery, search and rescue, custom agricultural applications. i will attach my current business card as well as some logos to incorporate for a new up to date business card
Updates

Designs look the same

Sick

Target Market(s)

farmers, hunters

Contact Information for Business Card

name address phone number (as existing card i attached)

Requirements
Must have
• im good with existing business card, but would like an agricultural twist

```html
<!DOCTYPE html>
<html lang="en">
<head>
<meta charset="utf-8">
<title>Korvane Sky Works – Business Card</title>
<link href="https://fonts.googleapis.com/css2?family=Montserrat:wght@400;500;600;700&display=swap" rel="stylesheet">
<style>
  :root {
    --page-bg: #e2e2e2;
    --leaf-green: #4b9547;
    --deep-green: #16281a;
    --card-black: #1b1b1b;
    --text-white: #f4f4f4;
    --muted-grey: #9a9a9a;
    --rule-grey: #5a5a5a;
  }
  * { box-sizing: border-box; margin: 0; padding: 0; }
  html, body { width: 1200px; height: 1200px; overflow: hidden; }
  body {
    background: var(--page-bg);
    font-family: "Montserrat", sans-serif;
    position: relative;
  }
  .card { position: absolute; left: 180px; width: 867px; height: 498px; }
  .card-front { top: 85px; background: var(--leaf-green); }
  .front-name {
    position: absolute; left: 0; right: 0; top: 205px;
    text-align: center; color: var(--deep-green);
    font-weight: 700; font-size: 48px; letter-spacing: 3px; line-height: 1.1;
    text-transform: uppercase;
  }
  .card-back { top: 625px; background: var(--card-black); overflow: hidden; }
  .top-band { position: absolute; left: 0; right: 0; top: 84px; height: 24px; background: var(--leaf-green); }
  .bottom-band { position: absolute; left: 0; right: 0; bottom: 0; height: 6px; background: var(--leaf-green); }
  .badge {
    position: absolute; left: 351px; top: 12px; width: 172px; height: 172px;
    border-radius: 50%; background: #ffffff;
    display: flex; align-items: center; justify-content: center;
  }
  .badge-name { color: var(--leaf-green); font-weight: 700; font-size: 24px; letter-spacing: 1px; }
  .services-heading {
    position: absolute; right: 456px; top: 205px;
    color: var(--leaf-green); font-weight: 700; font-size: 30px; letter-spacing: 1.5px; line-height: 1;
  }
  .service-list { list-style: none; }
  .service {
    position: absolute; right: 491px; color: var(--text-white);
    font-size: 22px; font-weight: 500; line-height: 1; white-space: nowrap;
  }
  .service::after {
    content: ""; position: absolute; right: -36px; top: 6px;
    width: 15px; height: 15px; background: var(--leaf-green);
  }
  .divider { position: absolute; left: 432px; top: 209px; width: 2px; height: 256px; background: var(--rule-grey); }
  .contact { position: absolute; left: 451px; top: 0; }
  .person-name {
    position: absolute; top: 207px; white-space: nowrap;
    color: var(--leaf-green); font-weight: 600; font-size: 30px; letter-spacing: 2px; line-height: 1;
  }
  .person-role { position: absolute; top: 242px; color: var(--muted-grey); font-size: 26px; line-height: 1; }
  .line {
    position: absolute; white-space: nowrap; color: var(--text-white);
    font-size: 23px; letter-spacing: 2px; line-height: 1;
  }
  .line .accent { color: var(--leaf-green); }
  .icon { position: absolute; left: 0; width: 26px; height: 26px; }
</style>
</head>
<body>
  <section class="card card-front">
    <h1 class="front-name">Korvane Sky Works</h1>
  </section>

  <section class="card card-back">
    <div class="top-band"></div>
    <div class="badge"><span class="badge-name">Korvane</span></div>

    <h2 class="services-heading">OUR SERVICES</h2>
    <ul class="service-list">
      <li class="service" style="top:262px">Thermal Image Inspections</li>
      <li class="service" style="top:322px">Deer Recovery</li>
      <li class="service" style="top:381px">Search &amp; Rescue</li>
      <li class="service" style="top:440px">Real Estate Photography</li>
    </ul>

    <div class="divider"></div>

    <div class="contact">
      <h3 class="person-name">DALEN VORST</h3>
      <p class="person-role">Owner</p>
      <p class="line" style="top:285px">214 W. Orchard St.</p>
      <p class="line" style="top:322px">Marlow OH 45990</p>

      <svg class="icon" style="top:363px" viewBox="0 0 24 24" aria-hidden="true">
        <path d="M6.5 2.5l3 3.5-2 2.2c1.2 2.8 3.5 5.1 6.3 6.3l2.2-2 3.5 3-2.2 3.2C10 19.5 4.5 14 3.3 4.7z" fill="none" stroke="#4b9547" stroke-width="1.8" stroke-linejoin="round"/>
        <path d="M14 3.5a7 7 0 0 1 6.5 6.5M14 7a3.5 3.5 0 0 1 3 3" fill="none" stroke="#4b9547" stroke-width="1.6" stroke-linecap="round"/>
      </svg>
      <p class="line" style="top:366px;left:41px">419 555 0142</p>

      <svg class="icon" style="top:401px" viewBox="0 0 24 24" aria-hidden="true">
        <g fill="none" stroke="#4b9547" stroke-width="1.5">
          <circle cx="12" cy="12" r="10"/>
          <ellipse cx="12" cy="12" rx="4.5" ry="10"/>
          <path d="M2 12h20M4 6.5h16M4 17.5h16M12 2v20"/>
        </g>
      </svg>
      <p class="line" style="top:404px;left:39px">www.<span class="accent">korvanedrone</span>.com</p>

      <svg class="icon" style="top:442px" viewBox="0 0 24 24" aria-hidden="true">
        <g fill="none" stroke="#4b9547" stroke-width="1.8" stroke-linejoin="round">
          <rect x="1.5" y="5" width="21" height="14"/>
          <path d="M1.5 5l10.5 8 10.5-8M1.5 19l8-7M22.5 19l-8-7"/>
        </g>
      </svg>
      <p class="line" style="top:443px;left:39px">korvanedrone@mail.com</p>
    </div>

    <div class="bottom-band"></div>
  </section>
</body>
</html>
```